Web Design Project: Facility Management company

Hi! We need a new website.

Our current website: http://www.vireo-trade.ru/ and we don-t like it. =)
The structure of our company has changed and now we don't need "cleaning" and "engeneering" on this site.

We are facility management company in Russia. So we provide integrated service solutions specific to industrial services: maintenance, repair, etc. of engineering systems.
More services:
Energy planning
Automation
Audit
Statements with regulators
Video surveillance
Central heating
Security systems
Welding
Management of subcontractors
Electrical installation and service needs
Reception
Catering

Visitors:
* Managers in the field of commercial real estate
* Chief engineers
* TOP managers of large companies, malls, factories...
+ their subordinates
* Small% of applicants.

Here you can see some websites/patterns we liked:
http://www.kobalmire.ru/ (This is our competitor’s site, so our site shouldn’t be an exact copy))))
http://www.dwatqo.ru/
http://www.layoutfarrow.com/demo/24296.html
http://www.layoutfarrow.com/website-templates/10145.html

Style:
Light, hi-tech/minimalizm, the color palette should be based on the original site colors (Green + black + white). http://www.vireo-trade.ru/

Estimated sitemap:
1. Home
2. About Us
3. Company's policy
4. History + Achievements.
5. Certificates
6. Map of presence (Here you can use sample map in file "our projects")
7. Services
8. Portfolio
9. News or blog
10. Jobs
11. Contacts - with the feedback form (or the function "call to order")
12. English

Need a design pages: main page, page 404. The rest of the page could be created by general pattern.

Logo, navigation bar and contacts should be visible on all pages of a site.
Flash animation elements and buttons, etc. - not needed.

* We need to develop 3 websites, so we are looking for a long term cooperation.
Looking forward to your creativity =)

Must Have:
Clear, intuitive structure of web pages.
In the center - of pictures reflecting our main services (industrial theme). May be in rotation.
BUT! This banner (central picture) should not be a huge one =)
All relevant information should be visible at once without scrolling.

A possibility to place media files (presentations, video ...) and 2 banner links on the main page.

Font should be available in Cyrillic.
Updates

IMPORTANT!

Please notice that in thisdesign we don't need "cleaning" and "engeneering" on this site.

So don't use old block of 4pictures from our current website. We don't need it anymore. 

Thestructure of our company has changed and now we need some links (may be banners,may be something else) to our future cleaning website as well as engeneeringwebsite.
It should look like seperate (partner) companies, not like our sevices.

Regards, Vera.

Please don't forget that we need bilingual site.

So define language changing tool in your designs.

Industry/Entity Type

Industrial

```html
<!DOCTYPE html>
<html lang="en">
<head>
<meta charset="utf-8">
<title>Vireo Service — Facility Management</title>
<link rel="stylesheet" href="https://fonts.googleapis.com/css2?family=Cabin:wght@400;500;600;700&family=PT+Sans:wght@400;700&display=swap">
<style>
:root{
  --nav-dark:#2c3a0b;
  --nav-mid:#3b4f12;
  --nav-active:#7e9b2c;
  --green:#86a22e;
  --green-light:#9bb53f;
  --green-deep:#5f7a1a;
  --panel:#7d9a2b;
  --ink:#3a3a3a;
  --ink-dark:#1e2e33;
  --btn:#2c3a0b;
  --btn-text:#a9c25a;
  --frame:#e9eae6;
  --footer:#232323;
  --footer-text:#8c8c8c;
  --white:#ffffff;
}
*{margin:0;padding:0;box-sizing:border-box}
html,body{width:1200px;height:933px;overflow:hidden;background:var(--white)}
body{position:relative;font-family:"PT Sans",Arial,sans-serif;color:var(--ink)}
.abs{position:absolute}

/* top navigation */
.topbar{left:0;top:0;width:1200px;height:47px;background:linear-gradient(var(--nav-mid),var(--nav-dark));border-bottom:1px solid #56701c}
.menu{left:110px;top:0;height:47px;display:flex;list-style:none;font-family:"Cabin",sans-serif;font-weight:600;font-size:13px;color:var(--white)}
.menu li{height:47px;line-height:50px;padding:0 12px;border-right:1px solid #26320a;box-shadow:1px 0 0 #4a6118;white-space:nowrap}
.menu li.active{background:linear-gradient(#93b03a,var(--nav-active));padding:0 16px;margin-top:5px;height:42px;line-height:40px;border:none;box-shadow:none}

/* header band */
.band{left:0;top:48px;width:1200px;height:405px;background:radial-gradient(ellipse 600px 260px at 600px 120px,var(--green-light),var(--green) 70%)}
.brand{left:111px;top:82px;display:flex;align-items:center;gap:10px;font-family:"Cabin",sans-serif;font-weight:700;font-size:27px;color:var(--white);letter-spacing:.5px}
.brand i{width:18px;height:18px;background:var(--white);display:block}
.helpbox{left:368px;top:68px;width:722px;height:61px;background:rgba(72,96,18,.35);border:1px solid rgba(255,255,255,.18);border-radius:4px}
.phone-icon{left:382px;top:78px}
.help-text{left:425px;top:76px;font-family:"Cabin",sans-serif;font-weight:600;color:#2f410c;line-height:1}
.help-text .big{font-size:24px;display:block}
.help-text .small{font-size:17px;display:block;margin-top:1px}
.phone{left:557px;top:81px;font-family:"Cabin",sans-serif;font-weight:700;font-size:30px;color:var(--white);letter-spacing:-.5px}
.search{left:789px;top:85px;width:177px;height:28px;background:var(--white);font:12px "PT Sans",sans-serif;color:#8a8a8a;padding:0 10px;line-height:28px}
.search-btn{left:966px;top:85px;width:25px;height:28px;background:var(--btn)}
.lang{left:1006px;top:86px;width:65px;height:26px;background:var(--btn);color:var(--btn-text);font:500 13px "Cabin",sans-serif;text-align:center;line-height:26px}

/* hero */
.hero{left:110px;top:147px;width:980px;height:357px;background:var(--frame);box-shadow:0 1px 3px rgba(0,0,0,.25)}
.hero-photo{left:126px;top:163px;width:948px;height:324px;background:linear-gradient(160deg,#3e6a8a 0%,#7fa6c2 40%,#c9dbe7 70%,#e6eef3 100%)}
.caption{left:126px;top:342px;width:712px;height:145px;background:linear-gradient(90deg,rgba(255,255,255,.55),rgba(255,255,255,.3) 80%,rgba(255,255,255,0))}
.caption h1{position:absolute;left:20px;top:20px;font:600 33px "Cabin",sans-serif;color:var(--ink-dark);letter-spacing:-.3px}
.caption p{position:absolute;left:20px;top:66px;width:640px;font:600 17px/23px "Cabin",sans-serif;color:var(--ink-dark)}

/* partner company links */
.partners{left:852px;top:395px;width:208px;display:flex;flex-direction:column;gap:8px}
.partner{display:flex;align-items:center;gap:10px;height:40px;padding:0 10px;background:rgba(255,255,255,.85);border-left:4px solid var(--panel);font-family:"Cabin",sans-serif;color:var(--ink-dark)}
.partner i{width:14px;height:14px;background:var(--panel);display:block;flex:none}
.partner b{display:block;font-weight:600;font-size:13px;line-height:15px}
.partner small{display:block;font-size:11px;line-height:13px;color:#5a6a45}

/* columns */
.col{top:528px;width:314px;height:310px;background:linear-gradient(#eef0e3,#ffffff 75%)}
.col h2{height:46px;background:var(--panel);border-radius:2px 2px 0 0;color:var(--white);font:600 18px/48px "Cabin",sans-serif;padding-left:16px}
.col-1{left:111px}.col-2{left:443px}.col-3{left:776px}
.ticks{list-style:none;margin:16px 0 0 14px}
.ticks li{position:relative;padding-left:17px;font-size:13px;line-height:22px}
.ticks li::before{content:"";position:absolute;left:1px;top:8px;width:6px;height:3px;border-left:1.5px solid var(--green-deep);border-bottom:1.5px solid var(--green-deep);transform:rotate(-45deg)}
.ticks.strong li{font:600 13px/22px "Cabin",sans-serif;color:#444}
.text{font-size:12px;line-height:20px;margin:0 22px 0 18px}
.col-1 .text{margin-top:9px}
.media{position:relative;margin:16px 0 0 18px;width:277px;height:63px;background:linear-gradient(100deg,#4a7490,#a5c3d8 55%,#dfe9f0)}
.media svg{position:absolute;left:124px;top:17px}
.media span{position:absolute;right:8px;bottom:5px;font:600 11px "Cabin",sans-serif;color:var(--ink-dark)}
.col-2 .text{margin-top:12px}
.col-2 .text+.text{margin-top:20px}
.lead{font:600 13px/22px "Cabin",sans-serif;color:#444;margin:13px 22px 0 14px}
.col-3 .ticks{margin:1px 16px 0 14px}
.col-3 .ticks li{font-size:12px;line-height:20px}
.col-3 .ticks li::before{top:7px}

/* footer */
.footer{left:0;top:869px;width:1200px;height:64px;background:var(--footer);text-align:center;font:13px "Cabin",sans-serif;color:var(--footer-text)}
.footer nav{margin-top:14px}
.footer nav span{margin:0 4px;color:#5a5a5a}
.footer .copy{margin-top:4px}
</style>
</head>
<body>

<div class="abs topbar"></div>
<ul class="abs menu">
  <li class="active">HOME</li>
  <li>ABOUT US</li>
  <li>COMPANY'S POLICY</li>
  <li>HISTORY + CERTIFICATES</li>
  <li>MAP</li>
  <li>SERVICES</li>
  <li>PORTFOLIO</li>
  <li>NEWS/BLOG</li>
  <li>JOBS</li>
  <li>CONTACT US</li>
</ul>

<div class="abs band"></div>

<div class="abs brand"><i></i>VIREO SERVICE</div>

<div class="abs helpbox"></div>
<svg class="abs phone-icon" width="38" height="42" viewBox="0 0 38 42" aria-hidden="true">
  <path d="M8 4c-4 2-6 6-5 11 2 9 9 19 18 24 4 2 8 1 10-2l2-3-7-6-4 3c-4-2-8-8-9-12l4-3-4-9z" fill="#2f410c"/>
</svg>
<div class="abs help-text"><span class="big">Need Help?</span><span class="small">Call us on:</span></div>
<div class="abs phone">+7 812 555 0148</div>
<div class="abs search">Enter a keyword...</div>
<div class="abs search-btn">
  <svg width="25" height="28" viewBox="0 0 25 28" aria-hidden="true"><circle cx="12" cy="13" r="7" fill="none" stroke="#a9c25a" stroke-width="2"/><line x1="17" y1="18" x2="21" y2="23" stroke="#a9c25a" stroke-width="2"/></svg>
</div>
<div class="abs lang">Русский</div>

<div class="abs hero"></div>
<div class="abs hero-photo" role="img" aria-label="Engineer in a hard hat and safety vest in front of glass skyscrapers under a blue sky"></div>
<div class="abs caption">
  <h1>QUALITY SERVICES ON TIME</h1>
  <p>We use an accumulated experience of immovable property maintenance, any kind of engineering systems, and their modernization for extension of durability time, and you save your money.</p>
</div>

<div class="abs partners">
  <a class="partner"><i></i><span><b>Vireo Clean</b><small>Partner cleaning company</small></span></a>
  <a class="partner"><i></i><span><b>Vireo Engineering</b><small>Partner engineering company</small></span></a>
</div>

<section class="abs col col-1">
  <h2>VIREO TM &amp; FM COMPANY</h2>
  <ul class="ticks strong">
    <li>Commercial property management</li>
    <li>Complex maintenance of immovable property</li>
    <li>Commercial property maintenance service</li>
  </ul>
  <p class="text">These are the most important aspects of acquisition of the highest possible incomes from the commercial property object´s operation regardless of their purpose: it can be production, business center, a building of a shop, bank, restaurant, warehousing logistic complex, hotel or the biggest shopping and recreation center.</p>
</section>

<section class="abs col col-2">
  <h2>WHY DO THEY CHOOSE US?</h2>
  <div class="media" role="img" aria-label="Video presentation slot: businessman on a phone beside office towers">
    <svg width="30" height="30" viewBox="0 0 30 30" aria-hidden="true"><circle cx="15" cy="15" r="14" fill="rgba(255,255,255,.85)"/><path d="M12 9l9 6-9 6z" fill="#5f7a1a"/></svg>
    <span>Company presentation</span>
  </div>
  <p class="text">Following the complex approach to management problems, we will help to optimize maintenance costs and your immovable property service.</p>
  <p class="text">We use an accumulated experience of immovable property maintenance, any kind of engineering systems, and their modernization for extension of durability time, and you save your money.</p>
</section>

<section class="abs col col-3">
  <h2>WHAT CAN WE DO?</h2>
  <p class="lead">Our own team of professionals will organize and provide:</p>
  <ul class="ticks">
    <li>Commercial property management</li>
    <li>Maintenance of immovable property</li>
    <li>Maintenance of dangerous industrial objects</li>
    <li>Maintenance and technical service of plants and factories</li>
    <li>Technical service of industrial and production equipment</li>
    <li>Energy planning, automation and audit of systems of any complexity</li>
    <li>Security systems and video surveillance</li>
  </ul>
</section>

<footer class="abs footer">
  <nav>Home <span>::</span> About us <span>::</span> Company's policy <span>::</span> History + Certificates <span>::</span> Services <span>::</span> Portfolio <span>::</span> News/blog <span>::</span> Jobs <span>::</span> Contact us</nav>
  <div class="copy">© Vireo Service 2010</div>
</footer>

</body>
</html>
```